【 概要 】 支援しているクライアントのクリニックの公式PIROのリッチメニューのデザインを募集します。 【 依頼内容 】 ・PIROリッチメニュー(2×3) ・作成数: 1種類 ・設定予定の項目 └Web受付・予約 └Free Wi-Fi └公式サイト └診療カレンダー └よくある質問 └お問い合わせ 【 デザインイメージ 】 ・メインターゲット:30~50代 女性(幅広い年齢層の患者さんがいます) ・雰囲気:水色ベースでユーザーが視覚的に使いやすいもの 【 契約金額(税抜) 】 ご希望の単価と合わせて提案ください ※契約金額(税込)からシステム利用料を差し引いた金額が、ワーカーさまの受取金額となります その他ご質問等ありましたら、気軽にお問い合わせください。 ご応募をお待ちしております! |
予約ボタンが鮮明だった点、シンプルの中にきれいさがあった点を評価し、この度は選ばせていただきました。
大変多くの数のご応募くださりありがとうございました!今後、似たような形でデザイン制作の募集等をする予定のため、また機会があればよろしくお願いいたします。

```html
<!DOCTYPE html>
<html lang="ja">
<head>
<meta charset="UTF-8">
<title>リッチメニュー</title>
<link href="https://fonts.googleapis.com/css2?family=Noto+Sans+JP:wght@300;400&display=swap" rel="stylesheet">
<style>
  :root {
    --sky-light: #b7d3f0;
    --sky-mid: #8db7e6;
    --sky-deep: #6a9bd8;
    --card-bg: #ffffff;
    --frame-line: #7b97c4;
    --corner: #86b1e3;
    --corner-deep: #5f8fd0;
    --label: #4d4d4d;
    --icon: #1c1c1c;
  }
  * { margin: 0; padding: 0; box-sizing: border-box; }
  html, body { width: 1200px; height: 810px; overflow: hidden; }
  body { font-family: "Noto Sans JP", sans-serif; }
  .rich-menu {
    position: relative;
    width: 1200px;
    height: 810px;
    background:
      radial-gradient(ellipse at 20% 30%, rgba(255,255,255,0.35), transparent 55%),
      radial-gradient(ellipse at 80% 75%, rgba(255,255,255,0.25), transparent 50%),
      radial-gradient(ellipse at 60% 10%, var(--sky-light), transparent 60%),
      linear-gradient(135deg, var(--sky-mid) 0%, var(--sky-light) 45%, var(--sky-deep) 100%);
  }
  .menu-item {
    position: absolute;
    width: 348px;
    height: 356px;
    background: var(--card-bg);
    box-shadow: 0 2px 6px rgba(40,80,140,0.18);
  }
  .menu-item::before {
    content: "";
    position: absolute;
    inset: 16px;
    border: 2px solid var(--frame-line);
  }
  .menu-item::after {
    content: "";
    position: absolute;
    right: 0;
    bottom: 0;
    width: 38px;
    height: 38px;
    background: linear-gradient(135deg, var(--corner) 0%, var(--corner-deep) 100%);
    clip-path: polygon(100% 0, 100% 100%, 0 100%);
  }
  .col-1 { left: 36px; }
  .col-2 { left: 424px; }
  .col-3 { left: 818px; }
  .row-1 { top: 28px; }
  .row-2 { top: 420px; }
  .menu-icon {
    position: absolute;
    left: 50%;
    top: 56px;
    width: 150px;
    height: 140px;
    transform: translateX(-50%);
  }
  .icon-placeholder {
    position: absolute;
    left: 50%;
    top: 56px;
    width: 140px;
    height: 140px;
    transform: translateX(-50%);
    background: radial-gradient(circle, #eef2f7 0%, #f8fafc 70%);
    border-radius: 8px;
  }
  .menu-label {
    position: absolute;
    left: 0;
    right: 0;
    top: 232px;
    text-align: center;
    font-size: 29px;
    font-weight: 300;
    letter-spacing: 0.12em;
    color: var(--label);
    white-space: nowrap;
  }
</style>
</head>
<body>
<main class="rich-menu">

  <a class="menu-item col-1 row-1">
    <div class="icon-placeholder" role="img" aria-label="スマートフォンを持つ手の線画イラスト"></div>
    <span class="menu-label">Web予約・受付</span>
  </a>

  <a class="menu-item col-2 row-1">
    <svg class="menu-icon" viewBox="0 0 140 130" fill="none" stroke="var(--icon)" stroke-width="7" stroke-linecap="round">
      <path d="M10 46 A84 84 0 0 1 130 46"/>
      <path d="M30 68 A56 56 0 0 1 110 68"/>
      <path d="M50 90 A28 28 0 0 1 90 90"/>
      <circle cx="70" cy="110" r="7" fill="var(--icon)" stroke="none"/>
    </svg>
    <span class="menu-label">Free Wi-Fi</span>
  </a>

  <a class="menu-item col-3 row-1">
    <svg class="menu-icon" viewBox="0 0 140 130" fill="none" stroke="var(--icon)" stroke-width="4">
      <circle cx="70" cy="65" r="52"/>
      <ellipse cx="70" cy="65" rx="22" ry="52"/>
      <line x1="70" y1="13" x2="70" y2="117"/>
      <line x1="26" y1="38" x2="114" y2="38"/>
      <line x1="26" y1="92" x2="114" y2="92"/>
      <rect x="8" y="52" width="124" height="26" rx="4" fill="var(--icon)"/>
      <rect x="14" y="56" width="94" height="18" fill="#fff" stroke="none"/>
      <text x="61" y="71" text-anchor="middle" font-family="Noto Sans JP, sans-serif" font-size="16" font-weight="400" fill="var(--icon)" stroke="none" letter-spacing="1">www</text>
      <circle cx="118" cy="63" r="5" stroke="#fff" stroke-width="2.5"/>
      <line x1="122" y1="67" x2="127" y2="72" stroke="#fff" stroke-width="2.5"/>
    </svg>
    <span class="menu-label">公式サイト</span>
  </a>

  <a class="menu-item col-1 row-2">
    <svg class="menu-icon" viewBox="0 0 140 130" fill="none" stroke="var(--icon)" stroke-width="6">
      <rect x="20" y="20" width="100" height="100" rx="12"/>
      <line x1="20" y1="42" x2="120" y2="42"/>
      <g stroke-width="5" stroke-linecap="round">
        <line x1="36" y1="10" x2="36" y2="28"/><line x1="54" y1="10" x2="54" y2="28"/>
        <line x1="70" y1="10" x2="70" y2="28"/><line x1="86" y1="10" x2="86" y2="28"/>
        <line x1="104" y1="10" x2="104" y2="28"/>
      </g>
      <g fill="var(--icon)" stroke="none">
        <rect x="42" y="54" width="10" height="10"/><rect x="58" y="54" width="10" height="10"/><rect x="74" y="54" width="10" height="10"/><rect x="90" y="54" width="10" height="10"/>
        <rect x="34" y="72" width="10" height="10"/><rect x="50" y="72" width="10" height="10"/><rect x="66" y="72" width="10" height="10"/><rect x="82" y="72" width="10" height="10"/><rect x="98" y="72" width="10" height="10"/>
        <rect x="34" y="90" width="10" height="10"/><rect x="50" y="90" width="10" height="10"/><rect x="66" y="90" width="10" height="10"/><rect x="82" y="90" width="10" height="10"/>
      </g>
    </svg>
    <span class="menu-label">診療カレンダー</span>
  </a>

  <a class="menu-item col-2 row-2">
    <svg class="menu-icon" viewBox="0 0 140 130" fill="none" stroke="var(--icon)" stroke-width="5" stroke-linejoin="round">
      <path d="M52 48 H124 Q130 48 130 54 V94 Q130 100 124 100 H116 V118 L100 100 H58 Q52 100 52 94 Z"/>
      <path d="M14 14 H88 Q96 14 96 22 V68 Q96 76 88 76 H40 L20 96 V76 H14 Q6 76 6 68 V22 Q6 14 14 14 Z" fill="#fff"/>
      <line x1="24" y1="34" x2="78" y2="34" stroke-linecap="round"/>
      <line x1="24" y1="54" x2="78" y2="54" stroke-linecap="round"/>
    </svg>
    <span class="menu-label">よくある質問</span>
  </a>

  <a class="menu-item col-3 row-2">
    <div class="icon-placeholder" role="img" aria-label="ヘッドセットを付けたオペレーターの線画アイコン"></div>
    <span class="menu-label">お問い合わせ</span>
  </a>

</main>
</body>
</html>
```